Following list to be designed:

1. A4 Letter Head

Must comprise of:
BRIGHT HARBOR and its LOGO
Address: No.41, 2F, Tarwin Plaza, Melrick Road, Upper Fenwood Gardens, Bangalore 560 017
Tel: 080 27481930
Fax: 080 27481931
Mail: query@brightharbor.example

Color of wordings to be in the lighter shade of blue and brighter shade of blue.

2. A4 Envelope

Must comprise of:
BRIGHT HARBOR and its LOGO
Tel: 080 27481930
Fax: 080 27481931

3. Postal Envelope

Must comprise of:
BRIGHT HARBOR and its LOGO
Tel: 080 27481930
Fax: 080 27481931

4. Business Card

Must comprise of:
Rohan Mehta
Managing Partner
Cell: +91 9487215043
Mail: rohanmehta@brightharbor.example
Tel: 080 27481930
Fax: 080 27481931

5. A4 Letter Head

Must comprise of:
BRIGHT HARBOR CORP. (wording) and BRIGHT HARBOR LOGO (only blue ribbon)

Blue ribbon (BRIGHT HARBOR LOGO) may be placed on Left Top Corner of the A4 Letter Head
and BRIGHT HARBOR CORP. (wording) to be placed on Right Top Corner of the A4 Letter Head

Tel: 080 27481930
Fax: 080 27481931

6. . A4 Envelope

Must comprise of:

Blue ribbon (BRIGHT HARBOR LOGO) may be placed on Left Top Corner of the A4 Envelope
and BRIGHT HARBOR CORP. (wording) to be placed on Right Top Corner of the A4 Envelope
Tel: 080 27481930
Fax: 080 27481931

Target Market(s)

Top IT/ITES Organizations

Industry/Entity Type

Real Estate Development

Font styles to use
Serif
Sans Serif

Colors
33a6d7
0792cd
85cae6

Requirements
Should not have
• Playful font and color

```html
<!DOCTYPE html>
<html lang="en">
<head>
<meta charset="utf-8">
<title>Bright Harbor Stationery</title>
<link rel="stylesheet" href="https://fonts.googleapis.com/css2?family=Source+Sans+3:wght@400;600&display=swap">
<style>
  :root {
    --backdrop: #d8d8d8;
    --paper: #ffffff;
    --brand-navy: #3d679e;
    --brand-sky: #63b6df;
    --ink: #3a3a3a;
    --icon-bg: #3d679e;
  }
  * { box-sizing: border-box; margin: 0; padding: 0; }
  html, body { width: 1200px; height: 1200px; overflow: hidden; }
  body {
    background: var(--backdrop);
    font-family: "Source Sans 3", sans-serif;
    color: var(--ink);
    position: relative;
  }
  .letterhead {
    position: absolute; left: 19px; top: 94px;
    width: 765px; height: 1080px;
    background: var(--paper);
  }
  .envelope {
    position: absolute; left: 352px; top: 228px;
    width: 810px; height: 524px;
  }
  .envelope-flap { position: absolute; left: 0; top: 0; width: 810px; height: 119px; }
  .envelope-body {
    position: absolute; left: 0; top: 119px;
    width: 810px; height: 405px;
    background: var(--paper);
  }
  .brand { position: absolute; }
  .brand-name {
    display: flex; align-items: center; gap: 8px;
    font-weight: 600; font-size: 26px; line-height: 1;
    color: var(--brand-navy); letter-spacing: 0.5px;
  }
  .brand-square { width: 14px; height: 14px; background: var(--brand-sky); }
  .brand-tagline {
    margin-top: 5px; margin-left: 22px;
    font-size: 9.5px; font-weight: 600; letter-spacing: 5.2px;
    color: var(--brand-navy);
  }
  .contact { position: absolute; font-size: 12.5px; line-height: 1.25; }
  .contact-address { margin-bottom: 10px; }
  .contact-row { display: flex; align-items: center; gap: 9px; margin-bottom: 8px; font-size: 13px; }
  .contact-icon { width: 17px; height: 17px; flex: none; }
  .letterhead .brand { left: 35px; top: 104px; }
  .letterhead .contact { left: 35px; top: 940px; }
  .envelope .brand { left: 16px; top: 82px; }
  .envelope .contact { left: 16px; top: 138px; }
</style>
</head>
<body>

<section class="letterhead" aria-label="Letterhead">
  <div class="brand">
    <div class="brand-name"><span class="brand-square"></span>BRIGHT HARBOR</div>
    <div class="brand-tagline">ASSET MANAGEMENT</div>
  </div>
  <div class="contact">
    <p class="contact-address">No.41, 2F, Tarwin Plaza, Melrick Road<br>Upper Fenwood Gardens, Bangalore 560 017</p>
    <div class="contact-row">
      <svg class="contact-icon" viewBox="0 0 17 17"><rect width="17" height="17" fill="var(--icon-bg)"/><path d="M5 4l2 0 1 3-1.5 1a6 6 0 0 0 2.5 2.5l1-1.5 3 1 0 2c-5 .5-8.5-3-8-8z" fill="none" stroke="#fff" stroke-width="1"/></svg>
      <span>080 27481930</span>
    </div>
    <div class="contact-row">
      <svg class="contact-icon" viewBox="0 0 17 17"><rect width="17" height="17" fill="var(--icon-bg)"/><rect x="5.5" y="3.5" width="6" height="3" fill="#fff"/><rect x="3.5" y="7" width="10" height="4.5" fill="#fff"/><rect x="5.5" y="10" width="6" height="3.5" fill="#fff" stroke="var(--icon-bg)" stroke-width="0.8"/></svg>
      <span>080 27481931</span>
    </div>
    <div class="contact-row">
      <svg class="contact-icon" viewBox="0 0 17 17"><rect width="17" height="17" fill="var(--icon-bg)"/><rect x="3.5" y="5" width="10" height="7" fill="#fff"/><path d="M3.5 5l5 4 5-4" fill="none" stroke="var(--icon-bg)" stroke-width="0.9"/></svg>
      <span>query@brightharbor.example</span>
    </div>
  </div>
</section>

<section class="envelope" aria-label="Envelope">
  <svg class="envelope-flap" viewBox="0 0 810 119" aria-hidden="true">
    <defs>
      <linearGradient id="flapGradient" x1="0" x2="1" y1="0" y2="0">
        <stop offset="0" stop-color="#3f6a9e"/>
        <stop offset="0.5" stop-color="#63b6df"/>
        <stop offset="1" stop-color="#3f6a9e"/>
      </linearGradient>
    </defs>
    <path d="M0 119 L30 16 Q35 0 55 0 L765 0 Q780 0 785 14 L810 119 Z" fill="url(#flapGradient)"/>
  </svg>
  <div class="envelope-body">
    <div class="brand">
      <div class="brand-name"><span class="brand-square"></span>BRIGHT HARBOR</div>
      <div class="brand-tagline">ASSET MANAGEMENT</div>
    </div>
    <div class="contact">
      <p class="contact-address">No.41, 2F, Tarwin Plaza, Melrick Road<br>Upper Fenwood Gardens, Bangalore 560 017</p>
      <div class="contact-row">
        <svg class="contact-icon" viewBox="0 0 17 17"><rect width="17" height="17" fill="var(--icon-bg)"/><path d="M5 4l2 0 1 3-1.5 1a6 6 0 0 0 2.5 2.5l1-1.5 3 1 0 2c-5 .5-8.5-3-8-8z" fill="none" stroke="#fff" stroke-width="1"/></svg>
        <span>080 27481930</span>
      </div>
      <div class="contact-row">
        <svg class="contact-icon" viewBox="0 0 17 17"><rect width="17" height="17" fill="var(--icon-bg)"/><rect x="5.5" y="3.5" width="6" height="3" fill="#fff"/><rect x="3.5" y="7" width="10" height="4.5" fill="#fff"/><rect x="5.5" y="10" width="6" height="3.5" fill="#fff" stroke="var(--icon-bg)" stroke-width="0.8"/></svg>
        <span>080 27481931</span>
      </div>
      <div class="contact-row">
        <svg class="contact-icon" viewBox="0 0 17 17"><rect width="17" height="17" fill="var(--icon-bg)"/><rect x="3.5" y="5" width="10" height="7" fill="#fff"/><path d="M3.5 5l5 4 5-4" fill="none" stroke="var(--icon-bg)" stroke-width="0.9"/></svg>
        <span>query@brightharbor.example</span>
      </div>
    </div>
  </div>
</section>

</body>
</html>
```